IT Company that provides secure IT solutions and services to our customers

We need business cards and a logo for a new IT Solutions company just created based in Kuala Lumpur, Malaysia. But will also be serving other countries in the region. We provide secure data, voice solutions on mobile platforms. Our first offering is encrypted voice and data solutions for ZUN, Pellovan, Quillet and Frondmoss devices.

Target Market(s)

large organizations Govt, Police, Defence, Anti-corruption, Legal, highly regulated industries such as Health-care, Financial, Banking, Insurance,

Industry/Entity Type

Information Technology

Contact Information for Business Card

VorlexIT (Logo - colour is ORVA blue)Rashid Nawfal Managing Director Kryption IT Sdn. Bhd.3rd Floor, Block C, Wisma LPN,No.14 Jalan Seri Hamzani,58410, Kuala LumpurMalaysia

Font styles to use
Sans Serif

Colors
3176b5
ec1f27
fbed22

Requirements
Must have
• VorlexIT all in Blue like ORVA blue. A logo design perhaps a play of VI, K with a dangling T (colour can be any)
Nice to have
• I want a clean crisp card, not too busy, easy to read.

```html
<!DOCTYPE html>
<html lang="en">
<head>
<meta charset="utf-8">
<title>VorlexIT Business Card</title>
<link href="https://fonts.googleapis.com/css2?family=Open+Sans:wght@400;600;700&display=swap" rel="stylesheet">
<style>
  :root {
    --page-bg: #e6e8eb;
    --brand-blue: #2f72b8;
    --brand-blue-light: #4b90d2;
    --mark-blue: #1e88d4;
    --card-white: #ffffff;
    --ink-dark: #333333;
    --text-on-blue: #ffffff;
    --divider-grey: #b8bcc2;
  }
  * { box-sizing: border-box; margin: 0; padding: 0; }
  html, body {
    width: 1200px; height: 900px; overflow: hidden;
    background: var(--page-bg);
    font-family: "Open Sans", Arial, sans-serif;
  }
  .canvas {
    position: relative; width: 1200px; height: 900px;
  }
  .card {
    position: absolute; left: 280px; width: 640px; height: 366px;
    box-shadow: 0 10px 28px rgba(0,0,0,.22);
    overflow: hidden;
  }
  .card-front {
    top: 64px;
    background: linear-gradient(120deg, var(--brand-blue) 0%, var(--brand-blue) 45%, var(--brand-blue-light) 100%);
    color: var(--text-on-blue);
    display: flex; flex-direction: column; align-items: center;
  }
  .card-front .brand {
    margin-top: 92px;
    display: flex; align-items: center; gap: 16px;
  }
  .brand-square {
    display: block; width: 58px; height: 58px;
  }
  .card-front .brand-square { background: var(--card-white); }
  .brand-name {
    font-weight: 600; font-size: 40px; letter-spacing: 1px; line-height: 1;
  }
  .card-front .website {
    margin-top: auto; margin-bottom: 58px;
    font-size: 15px; font-weight: 600; letter-spacing: .5px;
  }
  .card-back {
    top: 470px;
    display: flex;
  }
  .back-brand-panel {
    width: 250px; background: var(--card-white);
    display: flex; flex-direction: column; align-items: center; justify-content: center; gap: 22px;
  }
  .back-brand-panel .brand-square { width: 110px; height: 110px; background: var(--mark-blue); }
  .back-brand-panel .brand-name { color: var(--ink-dark); font-size: 36px; }
  .panel-divider {
    width: 10px; background: var(--divider-grey);
  }
  .details-panel {
    flex: 1;
    background: linear-gradient(120deg, var(--brand-blue) 0%, var(--brand-blue) 40%, var(--brand-blue-light) 100%);
    color: var(--text-on-blue);
    padding: 40px 30px 0 40px;
  }
  .person-name { font-weight: 700; font-size: 17px; }
  .person-title { font-size: 14px; margin-bottom: 16px; }
  .contact-list { list-style: none; }
  .contact-item {
    display: flex; align-items: flex-start; gap: 12px;
    font-size: 13.5px; line-height: 1.5; margin-bottom: 5px;
  }
  .contact-item.address { font-size: 12px; margin-bottom: 14px; }
  .contact-icon {
    flex: none; width: 18px; height: 16px; margin-top: 2px;
    background: var(--card-white); border-radius: 2px;
    display: flex; align-items: center; justify-content: center;
  }
  .contact-icon svg { width: 12px; height: 12px; fill: var(--brand-blue); }
</style>
</head>
<body>
<main class="canvas">
  <section class="card card-front">
    <div class="brand">
      <span class="brand-square"></span>
      <span class="brand-name">VorlexIT</span>
    </div>
    <p class="website">www.vorlexit.com</p>
  </section>

  <section class="card card-back">
    <div class="back-brand-panel">
      <span class="brand-square"></span>
      <span class="brand-name">VorlexIT</span>
    </div>
    <div class="panel-divider"></div>
    <div class="details-panel">
      <h1 class="person-name">Rashid Nawfal</h1>
      <p class="person-title">Managing Director</p>
      <ul class="contact-list">
        <li class="contact-item address">
          <span class="contact-icon"><svg viewBox="0 0 12 12"><path d="M6 1 L11 6 H9.5 V11 H7 V8 H5 V11 H2.5 V6 H1 Z"/></svg></span>
          <span>Vorlex IT Sdn. Bhd.3rd Floor, Block C,<br>Wisma LPN,No.14 Jalan Seri Hamzani,<br>58410, Kuala LumpurMalaysia</span>
        </li>
        <li class="contact-item">
          <span class="contact-icon"><svg viewBox="0 0 12 12"><path d="M1 4 Q6 0 11 4 L9.5 5.5 L8 4.5 H4 L2.5 5.5 Z M3 6 H9 L10 11 H2 Z"/></svg></span>
          <span>760-418-2257</span>
        </li>
        <li class="contact-item">
          <span class="contact-icon"><svg viewBox="0 0 12 12"><path d="M2 3 H10 V11 H2 Z M4 1 H8 V3 H4 Z"/></svg></span>
          <span>760-418-3390</span>
        </li>
        <li class="contact-item">
          <span class="contact-icon"><svg viewBox="0 0 12 12"><path d="M1 3 H11 V10 H1 Z M1 3 L6 7 L11 3" stroke="#ffffff" stroke-width=".8"/></svg></span>
          <span>info@vorlexit.com</span>
        </li>
        <li class="contact-item">
          <span class="contact-icon"><svg viewBox="0 0 12 12"><circle cx="6" cy="6" r="5"/><path d="M1 6 H11 M6 1 V11" stroke="#ffffff" stroke-width=".8"/></svg></span>
          <span>www.vorlexit.com</span>
        </li>
      </ul>
    </div>
  </section>
</main>
</body>
</html>
```